Gum Creek Critters business card and social media card

I would like 2 designs,

one with my logo that I have (attached file) for the front and then the chatterbook, Snapgallery and wanderguide icons on the back.I would like it to be eye catching.

The second design i would like the designers to come up with.I am looking for a colorful and eye catching but easy to read business card. I am in the center of Australia and would like earthy colors like orange/red, yellow, charcoal, brown, green etc. I would like a blue tongue lizard and a king brown snake in the design for the front. For the back I would like the Chatterbook, Snapgallery and wander guide logos.

Industry/Entity Type

Business

Contact Information for Business Card

Marcus Toller
CEO
GUM CREEK CRITTERS pty ltd
W: 041 907 2286
M: 048 216 0947
E: marcus@gumcreekcritters-example.com.au

Font styles to use
Other font styles liked:
• chiller

Colors
f37122
fbed22
ec1f27
474747
0492cd
acd036

Requirements
Must have
• Business name or my logo (attached file)
• Gum Creek Critters (in a cool font, like "chiller")
• Chatterbook icon
• Snapgallery icon
• Wanderguide icon
Nice to have
• Snake and a blue tongue lizard (either the full animals or just the heads)

```html
<!DOCTYPE html>
<html lang="en">
<head>
<meta charset="utf-8">
<title>Gum Creek Critters – Business Card</title>
<link href="https://fonts.googleapis.com/css2?family=Roboto:wght@400;500&family=Roboto+Condensed:wght@500&display=swap" rel="stylesheet">
<style>
  :root {
    --backdrop: #dedede;
    --card-white: #f4f4f4;
    --brand-red: #c8213a;
    --brand-orange: #f08a1c;
    --brand-gold: #e3b321;
    --charcoal: #474747;
    --rule-grey: #9a9a9a;
    --white: #ffffff;
  }
  * { margin: 0; padding: 0; box-sizing: border-box; }
  html, body { width: 1200px; height: 960px; overflow: hidden; }
  body {
    background: var(--backdrop);
    position: relative;
    font-family: "Roboto", Arial, sans-serif;
  }
  .card {
    position: absolute;
    width: 602px;
    height: 343px;
  }
  .card--front { left: 314px; top: 113px; background: var(--card-white); }
  .card--back  { left: 311px; top: 472px; width: 600px; background: var(--brand-red); }

  /* brand name block */
  .brand {
    position: absolute;
    display: flex;
    align-items: center;
    gap: 10px;
  }
  .brand__dot {
    width: 34px; height: 34px; border-radius: 50%;
    background: var(--brand-orange);
    flex: none;
  }
  .brand__name {
    font-family: "Roboto Condensed", "Arial Narrow", sans-serif;
    font-weight: 500;
    font-size: 30px;
    line-height: 32px;
    letter-spacing: 1px;
    text-transform: uppercase;
  }
  .card--front .brand { left: 366px; top: 48px; }
  .card--front .brand__name { color: var(--brand-red); }
  .card--back .brand { left: 190px; top: 104px; }
  .card--back .brand__name { color: var(--white); }

  /* person */
  .accent-bar {
    position: absolute; left: 0; top: 196px;
    width: 10px; height: 38px; background: var(--brand-red);
  }
  .person { position: absolute; left: 36px; top: 194px; }
  .person__name {
    font-family: "Roboto Condensed", "Arial Narrow", sans-serif;
    font-weight: 500; font-size: 21px; line-height: 24px;
    color: var(--brand-red); text-transform: uppercase;
  }
  .person__role {
    font-size: 14px; line-height: 18px; color: var(--brand-orange);
  }
  .divider {
    position: absolute; left: 36px; top: 247px;
    width: 527px; height: 1px; background: var(--rule-grey);
  }
  .contacts {
    position: absolute; left: 36px; top: 258px; list-style: none;
  }
  .contacts li {
    display: flex; align-items: center; gap: 8px;
    font-size: 14.5px; line-height: 19.5px; color: var(--charcoal);
  }
  .contacts svg { width: 13px; height: 13px; flex: none; fill: var(--brand-red); }
  .company-line {
    position: absolute; right: 38px; top: 298px;
    font-size: 11px; letter-spacing: 0.5px; color: var(--charcoal);
  }

  /* social row */
  .social {
    position: absolute; left: 0; right: 0; top: 284px;
    display: flex; justify-content: center; align-items: center; gap: 10px;
  }
  .social__line { width: 66px; height: 1px; background: rgba(255,255,255,0.6); }
  .social__item {
    display: flex; align-items: center; gap: 4px;
    font-size: 10.5px; color: var(--white);
  }
  .social__item::before {
    content: ""; width: 9px; height: 9px; border-radius: 50%;
    border: 1px solid var(--white);
  }
</style>
</head>
<body>
  <section class="card card--front" aria-label="Business card front">
    <div class="brand">
      <span class="brand__dot"></span>
      <span class="brand__name">Gum Creek<br>Critters</span>
    </div>
    <div class="accent-bar"></div>
    <div class="person">
      <p class="person__name">Marcus Toller</p>
      <p class="person__role">CEO</p>
    </div>
    <div class="divider"></div>
    <ul class="contacts">
      <li>
        <svg viewBox="0 0 24 24"><path d="M6.6 10.8c1.4 2.8 3.8 5.1 6.6 6.6l2.2-2.2c.3-.3.7-.4 1-.2 1.1.4 2.3.6 3.6.6.6 0 1 .4 1 1V20c0 .6-.4 1-1 1C10.6 21 3 13.4 3 4c0-.6.4-1 1-1h3.5c.6 0 1 .4 1 1 0 1.2.2 2.4.6 3.6.1.3 0 .7-.2 1l-2.3 2.2z"/></svg>
        041 907 2286
      </li>
      <li>
        <svg viewBox="0 0 24 24"><path d="M7 1h10a2 2 0 0 1 2 2v18a2 2 0 0 1-2 2H7a2 2 0 0 1-2-2V3a2 2 0 0 1 2-2zm0 3v14h10V4H7zm5 15.5a1 1 0 1 0 0 2 1 1 0 0 0 0-2z"/></svg>
        048 216 0947
      </li>
      <li>
        <svg viewBox="0 0 24 24"><path d="M2 5h20v14H2V5zm2 2v.5l8 5 8-5V7H4z"/></svg>
        marcus@gumcreekcritters-example.com.au
      </li>
    </ul>
    <p class="company-line">GUM CREEK CRITTERS pty ltd</p>
  </section>

  <section class="card card--back" aria-label="Business card back">
    <div class="brand">
      <span class="brand__dot"></span>
      <span class="brand__name">Gum Creek<br>Critters</span>
    </div>
    <div class="social">
      <span class="social__line"></span>
      <span class="social__item">Chatterbook</span>
      <span class="social__item">Snapgallery</span>
      <span class="social__item">Wanderguide</span>
      <span class="social__line"></span>
    </div>
  </section>
</body>
</html>
```